Electrical company needs professional eye catching business cards

I am an electrician who needs business cards. I have attached two images which you can use. The file ab.jpg I would atleast like to be used. The file named back.jpg can be used on the back or not... up to you.

The information on my business cards I will have displayed will be-
My name
Mobile number
web site url
Licence number
ABN

Also as another request, I would like the word "Electrician" on the front of the card somewhere. Maybe under my name or something?

Industry/Entity Type

Electrician

```html
<!DOCTYPE html>
<html lang="en">
<head>
<meta charset="utf-8">
<title>Kestrel Installations – Business Card</title>
<link rel="stylesheet" href="https://fonts.googleapis.com/css2?family=Raleway:wght@300;400;500;700;800&display=swap">
<style>
  :root {
    --navy: #213f92;
    --slate: #374862;
    --ink: #1c1c1c;
    --white: #ffffff;
    --grey-band: #a7a9ac;
    --backdrop: #e8e9ea;
  }
  * { margin: 0; padding: 0; box-sizing: border-box; }
  html, body {
    width: 1200px; height: 1200px; overflow: hidden;
    background: var(--backdrop);
    font-family: "Raleway", sans-serif;
    font-variant-numeric: lining-nums;
  }
  .canvas { position: relative; width: 1200px; height: 1200px; }

  .card {
    position: absolute; left: 174px; width: 851px; height: 487px; overflow: hidden;
  }
  .card--front { top: 68px; background: var(--white); }
  .card--back { top: 640px; background: var(--navy); }

  /* front */
  .edge-band { position: absolute; right: 0; width: 20px; background: var(--navy); }
  .edge-band--top { top: 0; height: 313px; }
  .edge-band--mid { top: 313px; height: 119px; background: var(--grey-band); }
  .edge-band--bottom { top: 432px; height: 55px; }

  .brand-name {
    position: absolute; font-weight: 500; font-size: 58px;
    letter-spacing: -0.5px; line-height: 1; white-space: nowrap;
  }
  .card--front .brand-name { left: 48px; top: 62px; color: var(--slate); }

  .person { position: absolute; left: 50px; top: 290px; }
  .person__name { font-weight: 300; font-size: 53px; color: var(--ink); line-height: 1; letter-spacing: 0.5px; }
  .person__role { margin-top: 6px; font-weight: 800; font-size: 24px; letter-spacing: 5.5px; color: var(--ink); line-height: 1; }

  .rule { position: absolute; left: 0; top: 423px; width: 434px; height: 8px; background: var(--navy); }

  .contacts { position: absolute; left: 454px; top: 304px; list-style: none; }
  .contacts li { display: flex; align-items: center; height: 34px; font-size: 24px; font-weight: 400; color: var(--ink); }
  .contacts svg { width: 22px; height: 22px; margin-right: 10px; flex: none; }

  /* back */
  .card--back .brand-name { left: 50%; top: 220px; transform: translateX(-50%); color: var(--white); }
  .legal { position: absolute; left: 58px; top: 380px; color: var(--white); font-size: 22px; line-height: 36px; font-weight: 400; }
</style>
</head>
<body>
<div class="canvas">
  <section class="card card--front">
    <div class="edge-band edge-band--top"></div>
    <div class="edge-band edge-band--mid"></div>
    <div class="edge-band edge-band--bottom"></div>

    <div class="brand-name">Kestrel Installations</div>

    <div class="person">
      <div class="person__name">Liam Carter</div>
      <div class="person__role">ELECTRICIAN</div>
    </div>

    <div class="rule"></div>

    <ul class="contacts">
      <li>
        <svg viewBox="0 0 22 22"><rect x="5" y="1" width="12" height="20" rx="2" fill="#213f92"/><rect x="7" y="4" width="8" height="12" fill="#fff"/></svg>
        000.000.0000
      </li>
      <li>
        <svg viewBox="0 0 22 22"><rect x="3" y="1" width="16" height="20" rx="2" fill="#213f92"/><rect x="6" y="4" width="10" height="5" fill="#fff"/><g fill="#fff"><rect x="6" y="11" width="2" height="2"/><rect x="10" y="11" width="2" height="2"/><rect x="14" y="11" width="2" height="2"/><rect x="6" y="15" width="2" height="2"/><rect x="10" y="15" width="2" height="2"/><rect x="14" y="15" width="2" height="2"/></g></svg>
        111.111.1111
      </li>
      <li>
        <svg viewBox="0 0 22 22" fill="none" stroke="#213f92" stroke-width="1.6"><circle cx="11" cy="11" r="9"/><ellipse cx="11" cy="11" rx="4" ry="9"/><line x1="2" y1="11" x2="20" y2="11"/><line x1="4" y1="6" x2="18" y2="6"/><line x1="4" y1="16" x2="18" y2="16"/></svg>
        www.kestrelinstallations.com
      </li>
      <li>
        <svg viewBox="0 0 22 22"><rect x="1" y="3" width="20" height="16" rx="2.5" fill="#213f92"/><rect x="4" y="6" width="14" height="10" fill="#fff"/></svg>
        liam@kestrelinstallations.com
      </li>
    </ul>
  </section>

  <section class="card card--back">
    <div class="brand-name">Kestrel Installations</div>
    <div class="legal">
      <div>0Licence No: xxxxxxxxx</div>
      <div>ABN xxxxxxxxx</div>
    </div>
  </section>
</div>
</body>
</html>
```